Tamberlin & Co Boutique Accommodation & Open Garden

Boutique Accommodation & Open garden; Weddings, Functions & Tours
A 1904 cottage is surrounded by 5 acres of landscaped gardens 3 of which are open to the public.
The many pathways entice it’s visitor to wonder under romantic rose covered arbours leading them to secluded flower filled areas.
The woodlands create a shady haven to rest in, while the pond at the bottom of the garden adds to the peace and tranquility felt by all in this harmonies spellbinding garden.

Open Thursday through Sunday, or by appointment.

I would like to down load my Logo. How do I do this?

Target Market(s)

Affluent

Colors

Designer to choose colors to be used in the design.

Requirements
Must have
• The Logo, Simplistic and classy.
• I am a graphic designer so have high expectations, but no time to do it myself. The design must be good.What to see and when.
Nice to have
• I am after a great design, must be classy must stand out. Not the run of the mill that everyone has.
Should not have
• Colours must complement Logo. Colours as in the saltwater @ narooma and black background with white writing.

```html
<!DOCTYPE html>
<html lang="en">
<head>
<meta charset="utf-8">
<title>Tamberlin &amp; Co – What To See &amp; When</title>
<link rel="stylesheet" href="https://fonts.googleapis.com/css2?family=Marcellus&family=Jost:wght@400;500&display=swap">
<style>
  :root {
    --sand: #fad9a9;
    --ink: #1a1a1a;
    --night: #000000;
    --gold: #e9c46c;
    --paper: #ffffff;
    --rule: #3a3a3a;
  }
  html, body { margin: 0; padding: 0; overflow: hidden; }
  body { width: 1200px; height: 853px; position: relative; background: var(--night); font-family: "Jost", sans-serif; }
  .guide { position: absolute; left: 0; top: 0; width: 403px; height: 853px; background: var(--sand); }
  .guide-title { position: absolute; left: 0; width: 403px; top: 44px; margin: 0; text-align: center; font-family: "Marcellus", serif; font-weight: 400; font-size: 25px; color: var(--ink); }
  .season-table { position: absolute; left: 31px; top: 91px; width: 358px; border-collapse: collapse; table-layout: fixed; font-size: 7.4px; line-height: 1.3; color: var(--ink); }
  .season-table th, .season-table td { border: 1px solid var(--rule); padding: 3px 4px; vertical-align: top; text-align: left; }
  .season-table th { font-weight: 400; text-align: center; height: 8px; padding: 2px; letter-spacing: .2px; }
  .season-table td { height: 40px; }
  .season-table col.month { width: 81px; }
  .season-table col.first { width: 141px; }
  .photo { position: absolute; }
  .thumb { top: 697px; height: 101px; box-shadow: 2px 2px 4px rgba(0,0,0,.35); }
  .thumb-garden { left: 31px; width: 177px; background: linear-gradient(180deg, #a9c3d6 0%, #6f8a58 55%, #4d5a3c 100%); }
  .thumb-range { left: 219px; width: 169px; background: linear-gradient(180deg, #c7d3da 0%, #8e9a8e 45%, #3f4f34 100%); }

  .feature-photo { top: 20px; height: 244px; }
  .p-open { left: 416px; width: 365px; background: linear-gradient(160deg, #6b4a2a 0%, #c4571e 35%, #3b3a22 70%, #1d2410 100%); }
  .p-wedding { left: 801px; width: 379px; background: linear-gradient(180deg, #cfd8d6 0%, #6d8a62 40%, #2b3a22 100%); }
  .p-stay { left: 416px; width: 365px; top: 421px; height: 255px; background: linear-gradient(180deg, #c9cbc8 0%, #55704a 40%, #2a3b20 80%, #9c3a55 100%); }
  .p-pond { left: 801px; width: 379px; top: 421px; height: 255px; background: linear-gradient(180deg, #2f74c4 0%, #7fa9d8 35%, #b98a4f 50%, #1d3f6d 75%, #2c5fa2 100%); }
  .inset { position: absolute; width: 126px; height: 126px; border-radius: 50%; border: 3px solid var(--paper); box-sizing: border-box; }
  .i-open { left: 655px; top: 187px; background: radial-gradient(circle, #e8ece6 0%, #7a8c6e 55%, #2e3a24 100%); }
  .i-wedding { left: 1050px; top: 185px; background: radial-gradient(circle, #d9dfdc 0%, #5c7350 60%, #26321d 100%); }
  .i-stay { left: 655px; top: 576px; background: radial-gradient(circle, #9fc17c 0%, #3f5a2c 70%, #1e2b14 100%); }
  .i-pond { left: 1048px; top: 576px; background: radial-gradient(circle, #d08a3a 0%, #3b6aa7 70%, #1e3a64 100%); }

  .feature-title { position: absolute; margin: 0; font-family: "Marcellus", serif; font-weight: 400; font-size: 18.5px; line-height: 22px; color: var(--gold); }
  .feature-text { position: absolute; margin: 0; font-size: 13.6px; line-height: 18.3px; color: var(--paper); text-align: justify; }
  .c-left { left: 431px; width: 350px; }
  .c-right { left: 825px; width: 353px; }
  .t-top { top: 292px; }
  .b-top { top: 320px; }
  .t-bot { top: 693px; }
  .b-bot { top: 720px; }
</style>
</head>
<body>
  <section class="guide">
    <h1 class="guide-title">What To See &amp; When</h1>
    <table class="season-table">
      <colgroup><col class="month"><col class="first"><col class="last"></colgroup>
      <tr><th>MONTH</th><th>FIRST FORTNIGHT</th><th>LAST FORTNIGHT</th></tr>
      <tr><td>October</td><td>Lots of spring flowers in blossom, Wisteria, Poppies, Citrus, Spring Annuals, Crabapples</td><td>Early Roses Iris, Water iris, Foxgloves, Cherry Blossom, Lilacs, Snowballs, Crabapples</td></tr>
      <tr><td>November</td><td>Crabapples, Roses, Water iris, Foxgloves, Elderberry Hedge</td><td>Roses, Flower borders, Lavenders, Delphiniums, Hawthorns</td></tr>
      <tr><td>December</td><td>Roses, Buddleia, Flower borders, Delphiniums</td><td>Roses, Buddleia, Flower borders, Lavenders, Hydrangeas, Gardenias</td></tr>
      <tr><td>January</td><td>Roses, Dahlias, Flower borders, Hydrangeas</td><td>Lilium Bulbs, Flower borders, Dahlias, Roses Hydrangeas</td></tr>
      <tr><td>February</td><td>Salvia, Flower borders, Dahlias, kitchen garden, Apples, Pears</td><td>Early Easter Daisy, Flower borders, Autumn Roses Dahlias</td></tr>
      <tr><td>March</td><td>Plectranthus, Belladonna Lilies, Buddleas, Salvias Dahlias, Autumn Roses</td><td>Fruit ripening on Apples &amp; pears, Autumn Roses Easter Daisy, Salvia, Flower borders</td></tr>
      <tr><td>April</td><td>Early Sasanqua Camellias, Flower borders, Early Autumn Tones</td><td>Flower borders, Early Apples &amp; Pears, Autumn Roses, Easter Daisy, Salvias</td></tr>
      <tr><td>May</td><td>Chrysanthemums, Autumn Colour, Mexican Sage</td><td>Sasanqua Camellias, Autumn Leaf Colour Mexican Sage</td></tr>
      <tr><td>June</td><td>Late autumn colour, Early Jonquils Citrus</td><td>Bare Pear Arbour</td></tr>
      <tr><td>July</td><td>Bare Winter Look, Bulbs, Magnolias</td><td>Very Wintery, Jonquils, Magnolias, Camellias</td></tr>
      <tr><td>August</td><td>Daphne, Jonquils Hedge, Magnolias, Bulbs, Camellias, Hellebores</td><td>Magnolias, Early Plum Blossom</td></tr>
      <tr><td>September</td><td>Forget-me-nots, Violets, Magnolias, Arum Lilies Freesias, Camellias, Wisteria, Pear Arbour</td><td>Azaleas, Bluebells, Lamberton Rose, Early Blossom, Bulbs, Freesias</td></tr>
    </table>
    <div class="photo thumb thumb-garden" role="img" aria-label="Garden path with clipped shrubs and flower beds under a blue sky"></div>
    <div class="photo thumb thumb-range" role="img" aria-label="Mountain range rising behind the garden trees"></div>
  </section>

  <div class="photo feature-photo p-open" role="img" aria-label="Autumn garden with red and orange maples beside a stone folly"></div>
  <div class="inset i-open" role="img" aria-label="White foxglove flowers close up"></div>
  <h2 class="feature-title c-left t-top">Open Garden</h2>
  <p class="feature-text c-left b-top">The essence of the gardens is one of romance, fairy tale like charm &amp; quaint English style elegance. With each season there are new wonders &amp; floral delights to explore.</p>

  <div class="photo feature-photo p-wedding" role="img" aria-label="Stone steps lined with topiary under a weeping willow"></div>
  <div class="inset i-wedding" role="img" aria-label="Wedding ceremony in a garden arbour"></div>
  <h2 class="feature-title c-right t-top">Weddings</h2>
  <p class="feature-text c-right b-top">Tamberlin Garden is the most exquisite wedding setting imaginable. With an opportunity for stunning photographs and videos, you will have beautiful memories that last forever.</p>

  <div class="photo feature-photo p-stay" role="img" aria-label="Misty garden lawn with pink hydrangeas and tall trees"></div>
  <div class="inset i-stay" role="img" aria-label="Green lawn path through a secluded garden"></div>
  <h2 class="feature-title c-left t-bot">Boutique Accommodation</h2>
  <p class="feature-text c-left b-bot">There are just a small handful of stunning &amp; elegantly designed rooms on offer, for those wishing to spend a night, or more, in the gorgeous surrounds. You will enjoy secluded areas to the secret garden, not open to the general public, including a picturesque creek flowing through.</p>

  <div class="photo feature-photo p-pond" role="img" aria-label="Still pond reflecting a mountain and autumn trees under blue sky"></div>
  <div class="inset i-pond" role="img" aria-label="Autumn tree reflected in the pond"></div>
  <h2 class="feature-title c-right t-bot">Pond</h2>
  <p class="feature-text c-right b-bot">A large section of grounds have been extensively and beautifully developed over many years, with water features, a garden folly and the Willow house over looking the tranquil pond. We look forward to welcoming you soon.</p>
</body>
</html>
```